Illustrations for a Project Management Concept

we need illustrations for 5 project management principles that make up a holistic approach to project management, without all the BS. if we extract all the methodology, system, tool and mumbo-jumbo out of project management, we end up with some essential principles that are simple to understand and use. It's likely that people who use them will not be traditional Project Management types.

I've mocked up something that looks very corporate based on a template, but this has the wrong tone; the wrong feeling. I'd like something "funky" and colorful that conveys "Action" within "Simplicity".

the PPT file with the dark-blue background is the "corporate" consulting type mockup. the PPT with the white background shows an idea I had for breaking out each of the 5 principles (only one shown) to make it larger, with some text in a callout.

In the final deliverable, I need to be able to both show all 5 on one diagram, as well as slicing the image to display each principle separately. i do not have editing capabilities for vector image formats, only image formats

Reason: there are a number of designers who have only just accepted the invitation. I want to give everyone a chance to submit.

```html
<!DOCTYPE html>
<html lang="en">
<head>
<meta charset="utf-8">
<title>Fulfill Customer Value, Interactively</title>
<link href="https://fonts.googleapis.com/css2?family=Jost:ital,wght@0,400;0,500;1,400&display=swap" rel="stylesheet">
<style>
  :root {
    --brand-orange: #ff6600;
    --paper: #ffffff;
    --soft-grey: #f2f2f2;
    --principle-green: #b3dbb5;
    --ink: #111111;
  }
  * { margin: 0; padding: 0; box-sizing: border-box; }
  html, body {
    width: 1200px;
    height: 834px;
    overflow: hidden;
    background: var(--brand-orange);
  }
  .principle-slide {
    position: relative;
    width: 1200px;
    height: 834px;
    background: var(--brand-orange);
    font-family: "Jost", "Futura", sans-serif;
    color: var(--ink);
  }
  .principle-shapes {
    position: absolute;
    inset: 0;
  }
  .principle-badge__label {
    position: absolute;
    left: 196px;
    top: 140px;
    width: 160px;
    text-align: center;
    font-size: 26px;
    line-height: 32px;
    font-weight: 400;
  }
  .principle-title {
    position: absolute;
    left: 400px;
    top: 288px;
    width: 415px;
    text-align: right;
    font-size: 21px;
    font-style: italic;
    line-height: 30px;
  }
  .principle-description {
    position: absolute;
    left: 330px;
    top: 343px;
    width: 560px;
    text-align: center;
    font-size: 17.6px;
    line-height: 25px;
  }
</style>
</head>
<body>
  <main class="principle-slide">
    <svg class="principle-shapes" width="1200" height="834" viewBox="0 0 1200 834" aria-hidden="true">
      <circle class="focus-circle" cx="608" cy="400" r="329" fill="var(--paper)"/>
      <circle class="focus-circle__core" cx="608" cy="400" r="200" fill="var(--soft-grey)"/>
      <path class="title-callout" d="M350 258 C372 276 398 281 432 281 H820 V324 H432 C392 324 362 300 350 258 Z" fill="var(--principle-green)"/>
      <circle class="principle-badge__ring" cx="276" cy="194" r="104" fill="var(--paper)"/>
      <circle class="principle-badge" cx="276" cy="194" r="94" fill="var(--principle-green)"/>
    </svg>

    <div class="principle-badge__label">Fulfill<br>Customer<br>Value</div>

    <h1 class="principle-title">2. Fulfill Customer Value, Interactively</h1>

    <p class="principle-description">Any activity, resource investment, or outcome that does not<br>service a customer value proposition is waste and probably<br>avoidable. The definition of value must be obtained<br>directly from the customer, not an intermediary. Project<br>deliverables must be validated with customers repeatedly<br>and directly.</p>
  </main>
</body>
</html>
```